Homepage design for Dutch Job Posting Site (Varo-Plek.nl)

We need a redesign of our homepage www.Varo-Plek.nl to make it very clear what we do. We are an online job posting portal and are looking to recruit clients and professionals on a single page.

The Homepage will focus on CLIENTS (OPDRACHTGEVERS), with the idea that if we have a lot of jobs posted, then the professionals will come.

Important to know is that we now have ONE REGISTRATION for both professionals and clients - so there is no need for two separate registration options.

Also important to know is that the JOB POSTER pages will have a GREEN hyperlinks color (see the color above the OPDRACHTGEVER at the top of the screen) and the Professionals will have a BLUE hyperlinks color (see the color above the PROFESSIONAL at the top of the screen).

At the top of the page, we would like a 4 page slider (we will do the coding but just want 4 slides) that shows how it works and what makes us unique. In the examples below, you can see that we have already done 2 of them, and we will ask the designer to help do the other two once the project is awarded.

You can see from the images provided that we have already done most of the work. The HEADER WRAP and the FOOTER are already done, and you can use these in your examples.

Notice also in the image "Homepage-BannerBlank" the image used in the center. It is an image that is only as wide as the header and then fades off into a background image that we can use repeat-x in the css of the site which fills the screen on any monitor resolution. If you don't understand what I just wrote, you probably are not the right designer for the job.

Notice also that the two images "NU AANMELDEN" and "VARO-PLEK ESCROW" use background images that have a SUBTLE background image - it is not just a gradient color change. This is what we LOVE in the design so far.

You can see that our design is already very far advanced, so what we are looking for in a new design are not the overall redesign, but specific, subtle design improvements to give the page a CLEAN, FRESH, MODERN look without being busy and crowded.

Where we specifically want help is in these areas. The designers that show us these elements will be the ones selected. All others will be eliminated without further comment:
a) How to blend in the Varo-Plek logo into the header design without taking up more HEIGHT (we have done a white overlay, but this is where you can prove to us that you are great.

b) We need a font for our h1 tags in our site. This will be the same font used in "Laatste Opdrachten" "Laatste Blogs" "Zoek uw professional per categorie of rubriek". Do not use a webfont (Arial or Verdana). Instead, refer to the examples provided for inspiration of a font that best suits the site for a header.

c) We need better containers for "Laatse opdrachten", "Laatste Blogs" and Zoek uw professional per categorie of rubriek. They can have colors or just borders or just outlines. They should compliment the site look though and not distract from it.

d) Transitions between the containers and other elements. Right now they are all just boxy and separate, but there could be some overlap, some shadows, an image divider (as there is between "Laatste Blogs" and TarnoRadio) but again, the transitions need top complement the design and not take it over.

Sites that appeal to us for what we are looking for are:
- brisket.com
- www.lumivault.com*
- Tallyforge.com*
- Quendalux.com*
*What we like here are both the top PROMINENT central message and then the smaller subtler design transitions underneath.

Feel free to use images or icons to complement the look, but it must be clean, fresh and modern.

Target Market(s)

University-educated Job Posters between 18 - 45

Industry/Entity Type

Online

Requirements
Must have
• - The header wrapper height but be exactly as it is on the images given. This header will be used on all the inner pages and therefore cannot be any higher than what is shown.
- Focus on the 4 tasks outlined
- Keep it clean! We love white, but also like small icons where appropriate and clean transitions.
Nice to have
• Dutch text is NOT important, we can translate.
Should not have
• No cluttered design.

```html
<!DOCTYPE html>
<html lang="nl">
<head>
<meta charset="utf-8">
<title>Varo-Plek.nl – Homepage</title>
<link rel="stylesheet" href="https://fonts.googleapis.com/css2?family=Arimo:ital,wght@0,400;0,700;1,400&family=Bebas+Neue&family=Roboto+Condensed:wght@400;700&family=Gelasio:ital@1&family=Open+Sans&display=swap">
<style>
:root{
  --page:#ebebeb;
  --card:#f9f9f9;
  --card-line:#d3d3d3;
  --divider:#e0e0e0;
  --text:#444;
  --meta:#333;
  --link-blue:#2a6db5;
  --green:#6a9a10;
  --green-light:#9fd200;
  --green-dark:#6f9c07;
  --sky:#8ec4f0;
  --sky-dark:#5ea2e0;
  --like:#5d76a8;
  --footer-bg:#f1f1ec;
  --footer-link:#8cbf1f;
  --footer-text:#666;
}
*{box-sizing:border-box;margin:0;padding:0}
html,body{width:1200px;height:900px;overflow:hidden}
body{background:var(--page);font-family:"Arimo",Arial,sans-serif;color:var(--text);position:relative}
.abs{position:absolute}

/* cards */
.card{position:absolute;left:110px;width:666px;background:var(--card);border:1px solid var(--card-line)}
.jobs{top:-2px;height:238px;border-top:none}
.entry{position:absolute;left:0;right:0}
.entry p{position:absolute;left:21px;width:605px;font-size:12.4px;line-height:18.5px;color:var(--text)}
.more{position:absolute;right:21px;font-size:12px;font-weight:700;color:var(--green);border-bottom:1px solid var(--green);line-height:13px;letter-spacing:.2px}
.rule{position:absolute;left:0;right:0;height:1px;background:var(--divider)}
.title{position:absolute;left:21px;font-family:"Roboto Condensed",Arial,sans-serif;font-size:17px;color:var(--link-blue);text-decoration:underline;text-underline-offset:3px;text-decoration-thickness:1px}
.title small{font-family:"Arimo",Arial,sans-serif;font-style:italic;font-size:12px;color:#333;text-decoration:none;display:inline-block;margin-left:6px}
.when{position:absolute;right:21px;font-size:12.5px;font-weight:700;color:var(--green)}
.when.lined{border-bottom:1px solid var(--green);line-height:13px}

.blogs{top:276px;height:393px;border-radius:7px 7px 0 0;border-top:none}
.blogs-head{position:absolute;left:-1px;right:-1px;top:0;height:56px;border-radius:7px 7px 0 0;background:linear-gradient(#a3d600,#86bd06 60%,#73a106)}
.blogs-head h1{position:absolute;left:17px;top:12px;font-family:"Bebas Neue",Impact,sans-serif;font-weight:400;font-size:34px;color:#fff;letter-spacing:.3px}
.blogs-head a{position:absolute;right:20px;top:19px;font-family:"Roboto Condensed",Arial,sans-serif;font-weight:700;font-size:17px;color:#3d5a07;letter-spacing:-.3px}
.meta{position:absolute;left:17px;font-size:12px;font-style:italic;color:var(--meta)}
.blogs .title{left:17px}
.blogs .entry p{left:17px;width:630px}
.blogs .more,.blogs .when{right:25px}

/* sidebar */
.side-top{left:803px;top:-4px;width:287px;height:11px;background:var(--green-dark);border-radius:0 0 5px 5px}
.like{left:803px;top:35px;width:287px;height:58px;background:var(--like);border:1px solid #3f5689;border-radius:3px}
.like p{position:absolute;left:8px;top:14px;font-size:12px;font-weight:700;color:#fff;line-height:15px}
.like span{position:absolute;right:10px;top:16px;width:81px;height:23px;background:#eef1f7;border:1px solid #c3cbdc;border-radius:2px;font-size:11.5px;color:#3b5998;line-height:21px;text-align:center}

.escrow{left:803px;top:125px;width:287px;height:339px;background:linear-gradient(#fbfbfb,#e9e9e9);border:1px solid #d6d6d6;border-radius:6px 6px 6px 6px}
.escrow-head{position:absolute;left:-1px;right:-1px;top:-1px;height:58px;border-radius:6px 6px 0 0;background:linear-gradient(#c6e2f8,#8ec4f0)}
.escrow-head h2{position:absolute;left:13px;top:14px;font-family:"Bebas Neue",Impact,sans-serif;font-weight:400;font-size:28px;color:#2f6ea8;letter-spacing:.5px}
.vault{position:absolute;right:14px;top:-19px;width:60px;height:76px;border-radius:4px;background:linear-gradient(135deg,#e4e6e8,#8d9194)}
.escrow h3{position:absolute;left:15px;top:73px;width:262px;font-size:14.4px;font-weight:700;color:#333;line-height:19px;letter-spacing:-.3px}
.point{position:absolute;left:14px;width:256px;border-top:1px solid #d6d6d6;padding:12px 0 0 13px;font-size:12.3px;line-height:18px;color:#555}
.point::before{content:"";position:absolute;left:0;top:14px;width:4px;height:14px;background:var(--green)}
.escrow-foot{position:absolute;left:-1px;right:-1px;bottom:-1px;height:29px;border-radius:0 0 6px 6px;background:linear-gradient(#9fcef5,#5ea2e0);font-size:12.5px;font-weight:700;color:#fff;text-align:right;padding:6px 20px 0 0}

/* radio banner */
.radio{left:110px;top:710px;width:980px;height:37px;border-radius:4px;background:linear-gradient(#3d3d3d,#232323)}
.radio .station{position:absolute;left:18px;top:-2px;width:123px;height:40px;background:#b51a1c;border:1px solid #7d0e10;color:#fff;font-family:"Arimo",Arial,sans-serif;font-weight:700;font-size:17px;line-height:38px;text-align:center}
.radio p{position:absolute;left:169px;top:7px;font-family:"Open Sans",sans-serif;font-size:18px;color:#fff}
.radio .fade{position:absolute;right:0;top:0;width:110px;height:37px;border-radius:0 4px 4px 0;background:linear-gradient(90deg,transparent,#555)}

/* footer */
.footer{left:0;top:799px;width:1200px;height:101px;background:var(--footer-bg);border-top:1px solid #d8d8d2;box-shadow:0 -2px 4px rgba(0,0,0,.08)}
.footer,.footer a{font-family:"Gelasio",Georgia,serif;font-style:italic;font-size:12.8px}
.footer a{color:var(--footer-link);text-decoration:none}
.footer .sep{color:#888;font-size:10px;margin:0 3px}
.mark{position:absolute;left:145px;top:25px;width:32px;height:32px;border-radius:50%;background:#9cc92c}
.copy{position:absolute;left:120px;top:67px;color:#555}
.vline{position:absolute;top:21px;width:1px;height:64px;background:#c9c9c4}
.links{position:absolute;left:245px;top:21px;line-height:21px;color:var(--footer-text)}
.stay{position:absolute;left:899px;top:20px;color:#555}
.social{position:absolute;left:899px;top:46px;display:flex;gap:10px}
.social span{display:flex;align-items:center;gap:4px;font-family:"Arimo",Arial,sans-serif;font-style:normal;font-size:11px;color:#555}
.social i{display:block;width:14px;height:14px;border-radius:2px}
</style>
</head>
<body>

<section class="card jobs">
  <div class="entry">
    <p style="top:-2px">instellen. Ik heb een Belvo online nummer, wat het vaste telefoonnummer moet worden, waarop alle medewerkers te bereiken zijn. Verder moet er doorverbonden kunnen worden naar specifi....</p>
    <a class="more" style="top:44px">OPDRACHT BEKIJKEN</a>
  </div>
  <div class="rule" style="top:78px"></div>
  <div class="entry">
    <a class="title" style="top:104px">Voip telefonie in kantoor instellen <small>( information technology )</small></a>
    <span class="when lined" style="top:108px">17 dagen geleden</span>
    <p style="top:136px">Voor mijn kantoor tot 5 werkplekken ben ik op zoek naar een bedrijf dat de telefonie voor mij op de juiste wijze kan instellen. Ik heb een Belvo online nummer, wat het vaste telefoonnummer moet worden, waarop alle medewerkers te bereiken zijn. Verder moet er doorverbonden kunnen worden naar specifi....</p>
    <a class="more" style="top:196px">OPDRACHT BEKIJKEN</a>
  </div>
</section>

<section class="card blogs">
  <header class="blogs-head"><h1>Laatste Blogs</h1><a>alles bekijken</a></header>
  <article class="entry">
    <a class="title" style="top:78px">Altijd ondernemer willen zijn</a>
    <span class="when" style="top:82px">1 maand geleden</span>
    <span class="meta" style="top:104px">Geschreven door Varo-Plek B.V. op woensdag 15 juni 2011 in Opdrachtgevers Escrow Varo-Plek | Reacties (0)</span>
    <p style="top:128px">Veel mensen dromen ervan om een eigen bedrijf te beginnen. Toch durven veel mensen de stap niet te zetten. Een bedrijf is bij de Kamer van Ondernemers binnen een half uur opgezet, maar dan? Hoe vind ik klanten? U breidt gestaag uw netwerk uit en voor u het weet kunt u fulltime voor uzelf aan de slag.</p>
    <a class="more" style="top:189px">LEES MEER ››</a>
  </article>
  <div class="rule" style="top:221px"></div>
  <article class="entry">
    <a class="title" style="top:245px">Altijd ondernemer willen zijn</a>
    <span class="when" style="top:249px">1 maand geleden</span>
    <span class="meta" style="top:271px">Geschreven door Varo-Plek B.V. op woensdag 15 juni 2011 in Opdrachtgevers Escrow Varo-Plek | Reacties (0)</span>
    <p style="top:295px">Veel mensen dromen ervan om een eigen bedrijf te beginnen. Toch durven veel mensen de stap niet te zetten. Een bedrijf is bij de Kamer van Ondernemers binnen een half uur opgezet, maar dan? Hoe vind ik klanten? U breidt gestaag uw netwerk uit en voor u het weet kunt u fulltime voor uzelf aan de slag.</p>
    <a class="more" style="top:356px">LEES MEER ››</a>
  </article>
</section>

<div class="abs side-top"></div>
<aside class="abs like">
  <p>Druk op "Vind ik leuk" om gelijk €<br>4,00 korting op uw abonnement</p>
  <span>Vind ik leuk</span>
</aside>

<aside class="abs escrow">
  <header class="escrow-head">
    <h2>VARO-PLEK ESCROW</h2>
    <div class="vault" role="img" aria-label="Illustratie van een geopende kluis"></div>
  </header>
  <h3>Met Varo-Plek Escrow bepaal u zelf wanner de profesional betaald wordt</h3>
  <div class="point" style="top:127px">Alleen u als opdrachtgever kunt htet geld overmaken naar de professional</div>
  <div class="point" style="top:186px">Uw opdracht wordt voltooid tot uw tevredenheid - of wordt het niet betaalt</div>
  <div class="point" style="top:246px">Met Varo-Plek Escrow, kan een mediator ingeschakeld worden in geval van geschil</div>
  <div class="escrow-foot">Gratis aanmelden ››</div>
</aside>

<div class="abs radio">
  <div class="station">TarnoRadio</div>
  <p>Zoals gehoord op TarnoRadio! Beluister direct onze radiospot</p>
  <div class="fade"></div>
</div>

<footer class="abs footer">
  <div class="mark"></div>
  <span class="copy">© 2011 Varo-Plek.nl</span>
  <div class="vline" style="left:229px"></div>
  <div class="links">
    Opdrachtgevers: <a>Plaats uw opdracht</a><span class="sep">/</span><a>Zoek professionals</a><span class="sep">/</span><a>Mijn Kantoor</a><br>
    Professionals: <a>Zoek opdrachten</a><span class="sep">/</span><a>Mijn Kantoor</a><br>
    Bedrijf: <a>Over Varo-Plek</a><span class="sep">/</span><a>Hoe het werkt</a><span class="sep">/</span><a>FAQ</a><span class="sep">/</span><a>Contact</a><span class="sep">/</span><a>Algemene voorwaarden</a><span class="sep">/</span><a>Privacy beleid</a><span class="sep">/</span><a>Geschillenregeling</a>
  </div>
  <div class="vline" style="left:879px"></div>
  <span class="stay">Stay Tuned on our Social Network</span>
  <div class="social">
    <span><i style="background:#3b5998"></i>Kringplein</span>
    <span><i style="background:#4fb3e0"></i>Fluitnet</span>
    <span><i style="background:#e8681d"></i>Nieuwsfeed</span>
  </div>
</footer>

</body>
</html>
```